Meadowgate Counselling Group Pty Ltd

clinical psychologist in private practice needs professional stationery package: business cards, complimentary slips, envelopes, range of business letterheads, and logo (photo of lighthouse).

I work with children, adolescents, adults and older population with a range of mental health concerns, adjustment to life transitions and learning difficulties. Majority of my correspondence is with medical practitioners writing reports. I would a clean crisp professional presentation (white background, navy blue text but open to ideas). Thought about having lighthouse as watermark on envelopes. My professional organisation (KRV) logo needs to be on business cards and templates (manual gives guidelines),. The photo of lighthouse is to be included in logo.
There needs to be three letterheads. 1.Is Company only Detail "meadowgate Counselling Group Pty Ltd". 2. Include Company detail and Fiona Hartwell Clinical Psychologist information at BQTG. 3. Include Company detail and Fiona Hartwell Clinical Psychologist information at Corran Vale Medical Centre

Target Market(s)

Doctors

Industry/Entity Type

Business

Colors
0355a3
3176b5
0592cd
33a6d7

Requirements
Must have
• Picture of the lighthouse
• KRV logo
• Business name

```html
<!DOCTYPE html>
<html lang="en">
<head>
<meta charset="utf-8">
<title>Meadowgate Counselling Group – Stationery Set</title>
<link href="https://fonts.googleapis.com/css2?family=Fira+Sans+Condensed:wght@400;500;600&family=Carlito:wght@400;700&family=Alegreya:wght@700&display=swap" rel="stylesheet">
<style>
:root{
  --navy:#0355a3;
  --blue:#1f5aa6;
  --ink:#1c1c1c;
  --board:#a7a7a7;
  --paper:#ffffff;
  --photo-sky:#5d8fc4;
  --photo-land:#6f7f56;
  --tower-light:#e6ecf1;
  --tower-shade:#c9d3dc;
  --cap:#f1b9b0;
}
*{box-sizing:border-box;margin:0;padding:0}
html,body{width:1200px;height:1000px;overflow:hidden}
body{background:var(--board);position:relative;font-family:"Fira Sans Condensed",sans-serif;color:var(--navy)}
.sheet{position:absolute;background:var(--paper);box-shadow:8px 10px 12px rgba(0,0,0,.45)}
.abs{position:absolute}
.photo{position:absolute;background:linear-gradient(180deg,var(--photo-sky) 0%,#a9c6e2 60%,var(--photo-land) 100%)}
.tower{position:absolute;background:linear-gradient(90deg,var(--tower-shade),var(--tower-light) 45%,var(--tower-shade));border-top:6px solid var(--cap)}
.co-name{font-weight:600;color:var(--navy);line-height:1.1}
.rule{position:absolute;height:2px;background:var(--navy)}
.krv{position:absolute;display:flex;align-items:center;gap:4px;color:#222;font-weight:500}
.krv i{display:block;border-radius:50%;background:#333}
.small{color:var(--navy);line-height:1.25}
.dark{color:#222}
.icon{display:inline-block;width:9px;height:9px;vertical-align:-1px;margin-right:4px}

/* business card */
.card{left:23px;top:18px;width:358px;height:222px}
.card .person{right:28px;top:26px;text-align:right;color:var(--blue)}
.card .person b{display:block;font-size:18px;font-weight:600}
.card .person span{font-size:14px}
.card .contact{left:28px;top:120px;font-size:11px;line-height:14px}

/* letterhead */
.letter{left:23px;top:265px;width:495px;height:700px;overflow:hidden}
.letter .body{left:37px;top:150px;width:425px;font-family:Carlito,sans-serif;font-size:10.2px;line-height:17.6px;color:var(--ink)}
.letter .body p{margin-bottom:10px}
.letter .footer{left:37px;top:637px;font-size:6px;line-height:8.3px}

/* comp slip */
.slip{left:610px;top:68px;width:550px;height:240px;overflow:hidden}
.slip h2{position:absolute;right:20px;top:13px;font-family:Alegreya,serif;font-size:18px;color:var(--navy)}

/* envelopes */
.env{left:556px;top:351px;width:604px;height:264px;overflow:hidden}
.env-back{left:556px;top:640px;width:604px;height:265px}
</style>
</head>
<body>

<!-- Business card -->
<section class="sheet card">
  <div class="photo" style="left:29px;top:27px;width:33px;height:40px" role="img" aria-label="Photo of a white lighthouse on a headland"></div>
  <div class="abs co-name" style="left:66px;top:40px;font-size:11px">MEADOWGATE COUNSELLING<br>Group Pty Ltd</div>
  <div class="abs person"><b>Fiona Hartwell</b><span>Clinical Psychologist</span></div>
  <div class="rule" style="left:27px;right:0;top:70px"></div>
  <div class="abs small" style="left:27px;top:74px;font-size:10.5px;font-weight:500">Navigating life's challenges: learning,<br>wellbeing, relationships and challenge</div>
  <div class="abs small" style="left:27px;top:100px;font-size:10.5px;font-weight:500">ABN: 47 318 550 916</div>
  <div class="abs contact small dark">
    <div><svg class="icon" viewBox="0 0 10 10"><path d="M1 3h8v5H1z" fill="#333"/></svg>00 0000 5172</div>
    <div><svg class="icon" viewBox="0 0 10 10"><rect x="1" y="2" width="8" height="7" fill="#333"/></svg>00 0000 5172</div>
    <div><svg class="icon" viewBox="0 0 10 10"><rect x="1" y="2" width="8" height="6" fill="none" stroke="#333"/><path d="M1 2l4 3 4-3" fill="none" stroke="#333"/></svg>admin@mailbox.com.au</div>
    <div><svg class="icon" viewBox="0 0 10 10"><circle cx="5" cy="5" r="4" fill="none" stroke="#333"/><path d="M1 5h8M5 1v8" stroke="#333"/></svg>www.sitelink.com.au</div>
    <div style="color:var(--navy);margin-top:2px;font-weight:500">Suite 6, 12 Abc St.<br>City Name, PB 4350</div>
  </div>
  <div class="krv" style="left:210px;top:150px;font-size:22px"><i style="width:22px;height:22px"></i>KRV</div>
</section>

<!-- Letterhead -->
<section class="sheet letter">
  <div class="tower" style="left:372px;top:380px;width:123px;height:320px" role="img" aria-label="Faint lighthouse watermark"></div>
  <div class="photo" style="left:42px;top:38px;width:50px;height:56px" role="img" aria-label="Photo of a white lighthouse on a headland"></div>
  <div class="abs co-name" style="left:96px;top:57px;font-size:14px">MEADOWGATE COUNSELLING<br>Group Pty Ltd</div>
  <div class="rule" style="left:40px;width:205px;top:97px"></div>
  <div class="abs small" style="left:40px;top:103px;font-size:6.6px">Navigating life's challenges: learning, wellbeing, relationships and challenge</div>
  <div class="abs small" style="left:40px;top:116px;font-size:6.6px">ABN: 47 318 550 916</div>
  <div class="abs small" style="left:304px;top:30px;font-size:6px;line-height:10px">
    <div style="font-size:11px;font-weight:600;line-height:13px">Fiona Hartwell</div>
    <div style="font-size:9.5px;line-height:12px">Clinical Psychologist</div>
    <div class="dark">BSc(Psych);BSc(Hons);GradDipEd;MEd;MPsych(Clinical)</div>
    <div class="dark">REG #PSY0004418207</div>
    <div class="dark">Medicare Provider # 7720415K &amp; 7720418B</div>
    <div>fiona.psy@mailnet.com</div>
    <div>Therapy and assessment for children, adolescents and adults</div>
  </div>
  <div class="abs body">
    <p style="margin-bottom:0">To</p>
    <p style="margin-bottom:0">Mr. Owen Petrakis</p>
    <p>Lorem Ipsum is simply a dummy text</p>
    <p>dummy text of the printing and typesetting industry. Lorem Ipsum has been the industry's standard dummy text ever since the 1500s, when an unknown printer took a galley of type and scrambled it to make a type specimen book. It has survived not only five centuries, but also the leap into electronic typesetting, remaining essentially unchanged. It was popularised in the 1960s with the release</p>
    <p>It is a long established fact that a reader will be distracted by the readable content of a page when lookidesktop publishing packages and web page editors now use Lorem Ipsum as their default model text, and a search for 'lorem ipsum' will uncover many web sites still in their infancy. Various versions have evolved over the years, sometimes by accident, sometimes on purpose (injected humour and the like).</p>
    <p>a Latin professor at Larkspur College in Virginia, looked up one of the more obscure Latin words, consectetur, from a Lorem Ipsum passage, and going through the cites of the word in classical literature, discovered the undoubtable source. Lorem Ipsum comes from sections 1.10.32 and 1.10.33 of "de Finibus Bonorum et Malorum" (The Extremes of Good and Evil) by Varenius, written in 45 BC. This book</p>
    <p>Lorem Ipsum</p>
    <div role="img" aria-label="Handwritten signature" style="width:125px;height:36px;background:linear-gradient(90deg,#e4e4e4,#cfcfcf);margin:-2px 0 12px"></div>
    <p>Lorem Ipsum is a dummy</p>
  </div>
  <div class="abs footer small">
    <div>Clinics: Fernleigh Street Mental Health, Suite 6, 18 Fernleigh St, ASHBURY, Q4350</div>
    <div>Clinics: Corran Vale Medical Centre, 27 Tarrant St, CORRAN VALE, Q4306</div>
    <div class="dark">Mail: PO Box 318, KELLWOOD, Q4352</div>
    <div class="dark">Tel: 07 5521 3907, Fax: 07 5521 3911</div>
    <div class="dark">Email: admin@bqtg.com.au, Web: www.bqtg.com.au</div>
  </div>
  <div class="krv" style="left:358px;top:645px;font-size:13px"><i style="width:12px;height:12px"></i>KRV <span style="font-size:6px;line-height:7px;border-left:1px solid #333;padding-left:3px">Member<br>KRV</span></div>
</section>

<!-- Compliments slip -->
<section class="sheet slip">
  <div class="tower" style="left:460px;top:58px;width:90px;height:182px" role="img" aria-label="Faint lighthouse watermark"></div>
  <div class="photo" style="left:18px;top:13px;width:24px;height:26px" role="img" aria-label="Photo of a white lighthouse on a headland"></div>
  <div class="abs co-name" style="left:45px;top:20px;font-size:7px">MEADOWGATE COUNSELLING<br>Group Pty Ltd</div>
  <div class="rule" style="left:18px;width:102px;top:40px;height:1.5px"></div>
  <div class="abs small" style="left:18px;top:44px;font-size:6px">Navigating life's challenges: learning,<br>wellbeing, relationships and challenge<br>ABN: 47 318 550 916</div>
  <h2>With Compliments</h2>
  <div class="abs small dark" style="left:20px;top:209px;font-size:5.5px;line-height:9px">07 5521 3907<br>07 5521 3907</div>
  <div class="abs" style="left:72px;top:206px;width:1px;height:22px;background:var(--navy)"></div>
  <div class="abs small dark" style="left:80px;top:209px;font-size:5.5px;line-height:9px">admin@bqtg.com.au<br>www.bqtg.com.au</div>
  <div class="abs" style="left:152px;top:206px;width:1px;height:22px;background:var(--navy)"></div>
  <div class="abs small" style="left:158px;top:209px;font-size:5.5px;line-height:9px">Suite 6, 18 Fernleigh St.<br>Ashbury, Q 4350</div>
  <div class="krv" style="left:466px;top:203px;font-size:10px"><i style="width:9px;height:9px"></i>KRV <span style="font-size:4.5px;line-height:5px">Member<br>KRV</span></div>
</section>

<!-- Envelope front -->
<section class="sheet env">
  <div class="tower" style="left:528px;top:72px;width:76px;height:192px" role="img" aria-label="Faint lighthouse watermark"></div>
  <div class="photo" style="left:20px;top:20px;width:22px;height:25px" role="img" aria-label="Photo of a white lighthouse on a headland"></div>
  <div class="abs co-name" style="left:45px;top:28px;font-size:6.5px">MEADOWGATE COUNSELLING<br>Group Pty Ltd</div>
  <div class="rule" style="left:19px;width:94px;top:45px;height:1.5px"></div>
  <div class="abs small" style="left:19px;top:48px;font-size:5.5px">Navigating life's challenges: learning,<br>wellbeing, relationships and challenge<br>ABN: 47 318 550 916</div>
  <div class="abs" style="left:125px;top:16px;width:1px;height:61px;background:var(--navy)"></div>
  <div class="abs small dark" style="left:132px;top:26px;font-size:5.5px;line-height:9px">admin@bqtg.com.au<br>www.bqtg.com.au</div>
  <div class="abs small" style="left:132px;top:50px;font-size:5.5px;line-height:9px">Suite 6, 18 Fernleigh St.<br>Ashbury, Q 4350</div>
</section>

<!-- Envelope back -->
<section class="sheet env-back">
  <svg class="abs" style="left:0;top:0" width="604" height="70" viewBox="0 0 604 70">
    <path d="M0 0 L48 62 Q50 65 56 65 L548 65 Q554 65 556 62 L604 0" fill="none" stroke="#5b87c8" stroke-width="1"/>
  </svg>
</section>

</body>
</html>
```